Design a peer-to-peer car rental marketplace website

Hello, would need in the next 24h the designs of the 4 following pages of a peer-to-peer car rental website called Wheelora (a website concept similar to [login to view URL]) :

- Homepage
- Results page
- Car details page
- Checkout

Find attached to the description THE BRIEF TO DOWNLOAD, the ideal fonts to use for the designs and the logo.

The winner will be hired again if he accepts, to design the rest of the pages for another project.

The conversion to HTML won’t be required but I will need the source files .ai, .psd or pdf after the contest.

I will be very active in the rating process, do not wait to finish all pages before submitting something. If you’re done with the homepage, submit it and we will work together.

Thanking in advance every freelancer for their time.

```html
<!DOCTYPE html>
<html lang="en">
<head>
<meta charset="utf-8">
<title>Wheelora — Peer-to-peer car rental</title>
<link href="https://fonts.googleapis.com/css2?family=Roboto:wght@400;500;700&display=swap" rel="stylesheet">
<style>
:root{
  --orange:#f26d21;
  --orange-light:#f7903a;
  --yellow:#f2b90f;
  --ink:#222;
  --text:#555;
  --muted:#999;
  --line:#e3e3e3;
  --gray-bg:#eeeeee;
}
*{box-sizing:border-box;margin:0;padding:0}
html,body{width:1200px;height:2511px;overflow:hidden}
body{position:relative;font-family:'Roboto',sans-serif;color:var(--text);background:#fff}
.abs{position:absolute}
.center{left:0;width:1200px;text-align:center}

/* top bar */
.topbar{top:0;left:0;width:1200px;height:29px;border-bottom:1px solid rgba(0,0,0,.06);z-index:2}
.topbar .address{left:165px;top:7px;font-size:11px;color:#333;display:flex;gap:8px;align-items:center}
.topbar .account{right:165px;top:0;height:29px;display:flex;font-size:11px;color:#333}
.topbar .account span{display:flex;align-items:center;gap:6px;padding:0 14px;border-left:1px solid rgba(0,0,0,.08)}
.topbar .account span:last-child{border-right:1px solid rgba(0,0,0,.08)}

/* hero */
.hero{top:0;left:0;width:1200px;height:535px;background:linear-gradient(180deg,#d8dccf 0%,#e9ece0 40%,#dfe3d4 70%,#cfd5c6 100%)}
.brand{left:165px;top:54px;font-size:36px;font-weight:700;color:var(--ink);letter-spacing:-1px}
.nav{right:315px;top:62px;display:flex;gap:23px;font-size:15px;color:#333}
.btn-rent{left:900px;top:55px;width:135px;height:36px;border-radius:18px;background:var(--orange);color:#fff;font-size:15px;font-weight:500;display:flex;align-items:center;justify-content:center}
.hero-title{top:190px;font-size:41px;font-weight:700;color:var(--orange)}
.hero-sub{top:246px;font-size:24px;font-weight:500;color:#222}
.hero-text{top:287px;font-size:16px;line-height:26px;color:#444}
.search{left:163px;top:376px;width:874px;height:108px;background:#fff;border-radius:6px;box-shadow:0 2px 8px rgba(0,0,0,.12)}
.field{position:absolute;top:24px;width:194px}
.field label{display:block;font-size:12px;font-weight:500;color:#333;margin-bottom:7px}
.field .input{height:37px;border:1px solid #ccc;display:flex;align-items:center;gap:8px;padding:0 8px;font-size:10px;color:#aaa}
.btn-search{position:absolute;left:656px;top:43px;width:194px;height:38px;background:linear-gradient(90deg,#222,#555);color:#fff;font-size:18px;display:flex;align-items:center;justify-content:center;border-radius:2px}

/* features */
.section-title{font-size:30px;font-weight:700;color:var(--orange)}
.section-title b{color:var(--ink)}
.feat-title{top:576px}
.feat-text{top:621px;font-size:15px;line-height:23px;color:#333}
.features{left:163px;top:703px;width:874px;height:120px;display:flex}
.feature{flex:1;text-align:center;border-right:1px solid var(--line);padding:8px 18px 0}
.feature:last-child{border-right:none}
.feature h3{font-size:17px;font-weight:500;color:#222;margin:10px 0 10px}
.feature p{font-size:11px;line-height:16px;color:#666}

/* featured cars */
.cars-band{top:868px;left:0;width:1200px;height:560px;background:linear-gradient(180deg,var(--gray-bg) 0%,#f6f6f6 50%,#ebebeb 100%)}
.big-title{font-size:40px;font-weight:700;color:var(--orange)}
.big-title b{color:var(--ink)}
.cars-title{top:912px}
.car{top:1003px;width:283px;height:285px;background:#fff;border-top:3px solid var(--orange);box-shadow:0 1px 3px rgba(0,0,0,.08)}
.car .photo{height:148px;background:linear-gradient(180deg,#8c95a0 0%,#4d5560 55%,#23272d 100%);position:relative}
.car .see{position:absolute;right:12px;bottom:7px;font-size:11px;color:#fff;display:flex;gap:4px;align-items:center}
.car h4{font-size:14px;font-weight:500;color:#222;margin:11px 12px 10px}
.car .meta{display:flex;margin:0 12px;font-size:11px;line-height:14px;color:#333}
.car .meta div{flex:1}
.car .meta small{display:block;color:#aaa;font-size:10px}
.car .price{display:flex;align-items:center;justify-content:space-between;margin:12px 12px 0;padding-top:10px;border-top:1px solid #eee}
.car .price span{font-size:10px;color:#aaa}
.car .price strong{font-size:19px;color:var(--orange);margin-left:6px}
.car .price a{font-size:11px;font-weight:500;color:#222;text-decoration:underline;margin-right:8px}
.btn-more{left:484px;top:1327px;width:231px;height:42px;border-radius:21px;background:var(--orange);color:#fff;font-size:17px;font-weight:500;display:flex;align-items:center;justify-content:center}

/* make money */
.money-title{top:1473px}
.offer{top:1567px;width:419px}
.offer .tile{height:268px;position:relative;color:#fff;text-align:center}
.offer .tile svg{position:absolute;left:167px;top:102px}
.offer .tile h3{position:absolute;left:0;right:0;top:211px;font-size:29px;font-weight:500}
.offer p{text-align:center;font-size:14px;line-height:21px;color:#555;padding:12px 50px 0;height:106px}
.offer .rule{height:5px}
.rent .tile{background:linear-gradient(135deg,var(--orange-light),#f26340)}
.rent .rule{background:#f2603a}
.park .tile{background:linear-gradient(135deg,#f4c320,#dfa20f)}
.park .rule{background:var(--yellow)}

/* testimonials */
.cust-title{top:2013px;font-size:27px;font-weight:700;color:var(--orange)}
.cust-title b{color:var(--ink)}
.cust-sub{top:2049px;font-size:14px;color:#444}
.name{top:2183px;font-size:15px;color:#222}
.quote{top:2218px;left:270px;width:660px;text-align:center;font-size:14px;line-height:25px;color:#555}
.dots{top:2346px;left:574px;display:flex;gap:7px}
.dots i{width:13px;height:13px;border-radius:50%;background:#ccc;display:block}
.dots i.on{background:var(--orange)}
</style>
</head>
<body>

<div class="abs hero" role="img" aria-label="Photo of a person sitting on a car in a green summer meadow with forested hills, washed in a light overlay"></div>

<div class="abs topbar">
  <div class="abs address">
    <svg width="9" height="13" viewBox="0 0 9 13"><path d="M4.5 0a4.5 4.5 0 0 0-4.5 4.5C0 8 4.5 13 4.5 13S9 8 9 4.5A4.5 4.5 0 0 0 4.5 0zm0 6.3a1.8 1.8 0 1 1 0-3.6 1.8 1.8 0 0 1 0 3.6z" fill="#333"/></svg>
    234 Fake, Fake city name, Country, 01234
  </div>
  <div class="abs account">
    <span><svg width="12" height="13" viewBox="0 0 12 13" fill="none" stroke="#333"><rect x="1" y="6" width="10" height="6.5"/><path d="M3 6V4a3 3 0 0 1 6 0v2"/></svg>Login</span>
    <span><svg width="13" height="13" viewBox="0 0 13 13" fill="none" stroke="#333"><circle cx="6.5" cy="4" r="3"/><path d="M1 12.5c0-3 2.5-5 5.5-5s5.5 2 5.5 5"/></svg>Sign up</span>
  </div>
</div>

<div class="abs brand">Wheelora</div>
<nav class="abs nav"><span>How it works</span><span>My bookings</span><span>Questions?</span></nav>
<div class="abs btn-rent">RENT MY CAR</div>

<h1 class="abs center hero-title">• LETS FIND A CAR AROUND YOU •</h1>
<h2 class="abs center hero-sub">AND BOOK IT FOR A FEW HOURS OR A FEW DAYS</h2>
<p class="abs center hero-text">This is Pixelmark's version &nbsp;of Lorem Ipsum. Proin gravida nibh vel velit auctor aliquet.<br>Aenean sollicitudin, lorem quis bibendum auctor</p>

<form class="abs search">
  <div class="field" style="left:26px"><label>Pick up location</label>
    <div class="input"><svg width="12" height="12" viewBox="0 0 12 12" fill="none" stroke="#aaa" stroke-width="1.3"><circle cx="5" cy="5" r="4"/><path d="M8 8l3.5 3.5"/></svg>Enter Airport, Hotel, Address etc...</div></div>
  <div class="field" style="left:236px"><label>Start date</label>
    <div class="input"><svg width="13" height="12" viewBox="0 0 13 12" fill="none" stroke="#bbb"><rect x=".5" y="1.5" width="12" height="10"/><path d="M.5 4.5h12"/></svg>MM/DD/YYYY 00:00</div></div>
  <div class="field" style="left:446px"><label>Return date</label>
    <div class="input"><svg width="13" height="12" viewBox="0 0 13 12" fill="none" stroke="#bbb"><rect x=".5" y="1.5" width="12" height="10"/><path d="M.5 4.5h12"/></svg>MM/DD/YYYY 00:00</div></div>
  <div class="btn-search">Search Now</div>
</form>

<h2 class="abs center section-title feat-title">FEATURES <b>&amp;</b> BENEFITS</h2>
<p class="abs center feat-text">This is Pixelmark's version &nbsp;of Lorem Ipsum. Proin gravida nibh vel velit auctor aliquet.<br>Aenean sollicitudin, lorem quis bibendum auctor</p>

<div class="abs features">
  <div class="feature">
    <svg width="30" height="26" viewBox="0 0 30 26" fill="var(--orange)"><rect x="9" y="0" width="12" height="3"/><rect x="3" y="7" width="24" height="4"/><rect x="8" y="14" width="14" height="3"/><rect x="0" y="21" width="30" height="4"/></svg>
    <h3>Flexibility</h3><p>This is Pixelmark's version &nbsp;of Lorem Ipsum. Proin gravida nibh.</p></div>
  <div class="feature">
    <svg width="26" height="26" viewBox="0 0 26 26" fill="none" stroke="var(--orange)" stroke-width="2.5"><circle cx="13" cy="13" r="10.5"/><path d="M13 7v6h-4"/></svg>
    <h3>Services</h3><p>This is Pixelmark's version &nbsp;of Lorem Ipsum. Proin gravida nibh.</p></div>
  <div class="feature">
    <svg width="28" height="26" viewBox="0 0 28 26" fill="var(--orange)"><rect x="0" y="0" width="3" height="26"/><path d="M3 2c6-3 10 3 16 0l9 1-3 6 3 7-9-1c-6 3-10-3-16 0z"/></svg>
    <h3>Freedom</h3><p>This is Pixelmark's version &nbsp;of Lorem Ipsum. Proin gravida nibh.</p></div>
  <div class="feature">
    <svg width="24" height="26" viewBox="0 0 24 26"><path d="M6 11V7a6 6 0 0 1 12 0v4" fill="none" stroke="var(--orange)" stroke-width="3"/><rect x="1" y="11" width="22" height="15" rx="1" fill="var(--orange)"/></svg>
    <h3>Security</h3><p>This is Pixelmark's version &nbsp;of Lorem Ipsum. Proin gravida nibh.</p></div>
</div>

<div class="abs cars-band"></div>
<h2 class="abs center big-title cars-title">• FEATURED <b>CARS</b> <span>•</span></h2>

<article class="abs car" style="left:164px">
  <div class="photo" role="img" aria-label="Photo of a dark blue hatchback parked by a stone wall"><span class="see"><svg width="11" height="9" viewBox="0 0 11 9" fill="#fff"><path d="M0 2h3l1-2h3l1 2h3v7H0z"/></svg>See Photos</span></div>
  <h4>Korvell Zeta IV kDi 90 - Diesel...</h4>
  <div class="meta"><div><small>Available at</small>Lenville-sur-Marne</div><div style="flex:.6"><small>Model Year</small>2015</div></div>
  <div class="price"><div><span>Price -</span><strong>38€/day</strong></div><a>View Details</a></div>
</article>
<article class="abs car" style="left:459px">
  <div class="photo" role="img" aria-label="Photo of a dark blue hatchback parked by a stone wall"><span class="see"><svg width="11" height="9" viewBox="0 0 11 9" fill="#fff"><path d="M0 2h3l1-2h3l1 2h3v7H0z"/></svg>See Photos</span></div>
  <h4>Korvell Zeta IV kDi 90 - Diesel...</h4>
  <div class="meta"><div><small>Available at</small>Lenville-sur-Marne</div><div style="flex:.6"><small>Model Year</small>2015</div></div>
  <div class="price"><div><span>Price -</span><strong>38€/day</strong></div><a>View Details</a></div>
</article>
<article class="abs car" style="left:752px">
  <div class="photo" role="img" aria-label="Photo of a dark blue hatchback parked by a stone wall"><span class="see"><svg width="11" height="9" viewBox="0 0 11 9" fill="#fff"><path d="M0 2h3l1-2h3l1 2h3v7H0z"/></svg>See Photos</span></div>
  <h4>Korvell Zeta IV kDi 90 - Diesel...</h4>
  <div class="meta"><div><small>Available at</small>Lenville-sur-Marne</div><div style="flex:.6"><small>Model Year</small>2015</div></div>
  <div class="price"><div><span>Price -</span><strong>38€/day</strong></div><a>View Details</a></div>
</article>

<div class="abs btn-more">FIND MORE CARS</div>

<h2 class="abs center big-title money-title">• MAKE MONEY WITH YOUR CAR •</h2>

<section class="abs offer rent" style="left:164px">
  <div class="tile" role="img" aria-label="Orange-tinted photo of a person working on a laptop">
    <svg width="85" height="85" viewBox="0 0 85 85"><circle cx="42.5" cy="42.5" r="40" fill="none" stroke="#fff" stroke-width="4"/><text x="42.5" y="56" text-anchor="middle" font-family="Roboto,sans-serif" font-weight="700" font-size="40" fill="#fff">€</text></svg>
    <h3>RENT YOUR CAR</h3>
  </div>
  <p>This is Pixelmark's version &nbsp;of Lorem Ipsum. Proin gravida nibh vel velit auctor aliquet. Aenean sollicitudin, lorem quis bibendum auctor.</p>
  <div class="rule"></div>
</section>
<section class="abs offer park" style="left:616px">
  <div class="tile" role="img" aria-label="Yellow-tinted photo of an indoor parking garage">
    <svg width="85" height="85" viewBox="0 0 85 85"><circle cx="42.5" cy="42.5" r="40" fill="none" stroke="#fff" stroke-width="4"/><text x="42.5" y="57" text-anchor="middle" font-family="Roboto,sans-serif" font-weight="700" font-size="40" fill="#fff">P</text></svg>
    <h3>PARK AND EARN</h3>
  </div>
  <p>This is Pixelmark's version &nbsp;of Lorem Ipsum. Proin gravida nibh vel velit auctor aliquet. Aenean sollicitudin, lorem quis bibendum auctor.</p>
  <div class="rule"></div>
</section>

<h2 class="abs center cust-title">• HAPPY <b>CUSTOMERS</b> •</h2>
<p class="abs center cust-sub">What Our Customers Are Saying</p>
<svg class="abs" style="left:566px;top:2102px" width="68" height="68" viewBox="0 0 68 68"><circle cx="34" cy="34" r="32.5" fill="#fff" stroke="#ccc" stroke-width="3"/><circle cx="34" cy="27" r="7" fill="var(--orange)"/><path d="M21 45c0-7 6-10 13-10s13 3 13 10z" fill="var(--orange)"/></svg>
<p class="abs center name">John Doe</p>
<p class="abs quote">This is Pixelmark's version &nbsp;of Lorem Ipsum. Proin gravida nibh vel velit auctor aliquet. Aenean sollicitudin, lorem quis bibendum auctor, nisi elit consequat ipsum, nec sagittis sem nibh id elit. Duis sed odio sit amet nibh vulputate cursus a sit amet mauris.</p>
<svg class="abs" style="left:200px;top:2250px" width="40" height="20" viewBox="0 0 40 20" fill="none" stroke="#bbb" stroke-width="2"><path d="M39 10H2M10 2L2 10l8 8"/></svg>
<svg class="abs" style="left:960px;top:2250px" width="40" height="20" viewBox="0 0 40 20" fill="none" stroke="#bbb" stroke-width="2"><path d="M1 10h37M30 2l8 8-8 8"/></svg>
<div class="abs dots"><i></i><i class="on"></i><i></i></div>

</body>
</html>
```